Business Card for Quillmark Ledger - A cannabis publication for executives.

I'd like some business cards for Quillmark Ledger. The logo is done (great job!) and I need a card design I will use with PRINTLY. I made it a short project to allow time for printing before an event. These will be standard sized cards (final artwork size 3.66" x 2.16" at 300dpi) with a final card size of 3.5" x 2.0". (See PRINTLY.com if you need more info.) I might try rounded corners but am not sure yet. I think the design will work okay with rounded.

Quillmark Ledger will be a bi-weekly publication for the cannabis industry. It is targeted to investors and industry executives, not consumers or pot smokers. So our market is more B2B. However I am open to creativity and making the card something people remark on.

My contact for card:

Dana Merrow
Founder/CEO
dana@quillmarkledger.example

2740 Harlow Avenue
Boston MA 02135
(617)555-0194

Target Market(s)

Executives, Industry people and investors in the Cannabis sector.

Contact Information for Business Card

PRINTLY does do double sided and the second side can be the same or different images. Only one side is required but use of the second side would be a bonus.

Font styles to use
Serif
Sans Serif
Decorative

Colors

Designer to choose colors to be used in the design.

Requirements
Must have
• Logo, contact info
Nice to have
• Style and design to make the card stand out in a crowd.

```html
<!DOCTYPE html>
<html lang="en">
<head>
<meta charset="utf-8">
<title>Quillmark Ledger – Business Card</title>
<link href="https://fonts.googleapis.com/css2?family=Merriweather:wght@700&family=Arimo:wght@400&display=swap" rel="stylesheet">
<style>
  :root {
    --brand-green: #84b036;
    --paper: #ffffff;
    --ink: #2b2b2b;
    --ink-soft: #555555;
    --divider: #333333;
    --backdrop: #ffffff;
    --shadow: rgba(0, 0, 0, 0.28);
  }
  html, body {
    margin: 0;
    padding: 0;
    width: 1200px;
    height: 1001px;
    overflow: hidden;
    background: var(--backdrop);
  }
  .canvas {
    position: relative;
    width: 1200px;
    height: 1001px;
  }
  .card {
    position: absolute;
    top: 376px;
    width: 436px;
    height: 248px;
    border-radius: 36px;
    overflow: hidden;
    box-shadow: 0 6px 16px var(--shadow);
  }
  .card--front {
    left: 104px;
    background: var(--brand-green);
  }
  .card--back {
    left: 660px;
    background: var(--paper);
  }
  .wordmark {
    position: absolute;
    left: 0;
    right: 0;
    display: flex;
    align-items: center;
    justify-content: center;
    gap: 12px;
    font-family: "Merriweather", Georgia, serif;
    font-weight: 700;
    white-space: nowrap;
  }
  .wordmark__dot {
    border-radius: 50%;
    flex: none;
  }
  .card--front .wordmark {
    top: 100px;
    font-size: 31px;
    color: var(--paper);
  }
  .card--front .wordmark__dot {
    width: 30px;
    height: 30px;
    background: var(--paper);
  }
  .card--back .wordmark {
    top: 48px;
    font-size: 24px;
    color: var(--brand-green);
  }
  .card--back .wordmark__dot {
    width: 24px;
    height: 24px;
    background: var(--brand-green);
  }
  .contact {
    font-family: "Arimo", Arial, Helvetica, sans-serif;
    position: absolute;
  }
  .person {
    left: 92px;
    top: 139px;
  }
  .person__name {
    font-size: 17px;
    color: var(--ink);
    line-height: 20px;
  }
  .person__title {
    font-size: 13px;
    color: var(--ink-soft);
    line-height: 18px;
  }
  .divider {
    position: absolute;
    left: 217px;
    top: 124px;
    width: 2px;
    height: 64px;
    background: var(--divider);
  }
  .reach {
    left: 241px;
    top: 143px;
    font-size: 12.5px;
    color: var(--ink-soft);
    line-height: 18px;
  }
  .address-band {
    position: absolute;
    left: 0;
    right: 0;
    bottom: 0;
    height: 26px;
    background: var(--brand-green);
    color: var(--paper);
    font-family: "Arimo", Arial, Helvetica, sans-serif;
    font-size: 13px;
    line-height: 26px;
    text-align: center;
    letter-spacing: 0.2px;
  }
</style>
</head>
<body>
<main class="canvas">
  <section class="card card--front" aria-label="Card front">
    <div class="wordmark"><span class="wordmark__dot"></span>Quillmark Ledger</div>
  </section>

  <section class="card card--back" aria-label="Card back">
    <div class="wordmark"><span class="wordmark__dot"></span>Quillmark Ledger</div>
    <div class="contact person">
      <div class="person__name">Dana Merrow</div>
      <div class="person__title">Founder/CEO</div>
    </div>
    <div class="divider"></div>
    <div class="contact reach">
      <div class="reach__phone">(617)555-0194</div>
      <div class="reach__email">dana@quillmarkledger.example</div>
    </div>
    <div class="address-band">2740 Harlow Avenue Boston MA 02135</div>
  </section>
</main>
</body>
</html>
```